agricultural technology company needs business cards*

design a business card that represents our business well. please see our website: vastrelbyfieldseal.com.au
professional, simple, clean lines, not complicated or floral.....

```html
<!DOCTYPE html>
<html lang="en">
<head>
<meta charset="utf-8">
<title>Vastrelby Fieldseal – Business Card</title>
<link rel="stylesheet" href="https://fonts.googleapis.com/css2?family=Montserrat:wght@600;800&family=Open+Sans:wght@400;600&display=swap">
<style>
  :root {
    --navy: #1c2a5c;
    --navy-deep: #17234d;
    --navy-soft: #2c3d78;
    --green: #2bb24c;
    --ink: #24305e;
    --white: #ffffff;
    --stage: #e6e7ea;
  }
  * { box-sizing: border-box; margin: 0; padding: 0; }
  html, body { width: 1200px; height: 1124px; overflow: hidden; }
  body {
    background: var(--stage);
    font-family: "Open Sans", Arial, sans-serif;
    position: relative;
  }
  .card {
    position: absolute;
    left: 190px;
    width: 820px;
    height: 500px;
    border-bottom: 6px solid var(--green);
    box-shadow: 0 6px 18px rgba(0,0,0,.18);
  }
  .card--back {
    top: 40px;
    background: var(--navy);
  }
  .card--front {
    top: 584px;
    background: var(--white);
    border-left: 6px solid var(--green);
  }

  /* back */
  .back-name {
    position: absolute;
    left: 190px;
    top: 170px;
    font-family: "Montserrat", Arial, sans-serif;
    font-weight: 800;
    font-size: 58px;
    line-height: 1.02;
    color: var(--navy-soft);
  }
  .back-web {
    position: absolute;
    right: 60px;
    bottom: 48px;
    font-size: 20px;
    color: #c9d0e6;
    letter-spacing: .3px;
  }

  /* front */
  .brand {
    position: absolute;
    left: 60px;
    top: 190px;
    display: flex;
    align-items: center;
    gap: 14px;
  }
  .brand-mark {
    width: 22px; height: 22px;
    background: var(--green);
    border-radius: 50%;
    flex: none;
  }
  .brand-name {
    font-family: "Montserrat", Arial, sans-serif;
    font-weight: 800;
    font-size: 38px;
    line-height: 1.05;
    color: var(--navy);
  }
  .divider {
    position: absolute;
    left: 418px;
    top: 120px;
    width: 2px;
    height: 196px;
    background: var(--navy);
  }
  .details {
    position: absolute;
    left: 444px;
    top: 118px;
    color: var(--ink);
  }
  .person-name {
    font-family: "Montserrat", Arial, sans-serif;
    font-weight: 600;
    font-size: 27px;
    color: var(--green);
    letter-spacing: .5px;
  }
  .person-role {
    font-size: 21px;
    margin-top: 0;
  }
  .address {
    font-size: 20px;
    line-height: 1.3;
    margin-top: 18px;
    font-style: normal;
  }
  .contacts { list-style: none; margin-top: 16px; }
  .contacts li {
    display: flex;
    align-items: center;
    gap: 12px;
    font-size: 20px;
    line-height: 1.4;
  }
  .contacts svg { width: 18px; height: 18px; flex: none; }
</style>
</head>
<body>

  <section class="card card--back" aria-label="Business card back">
    <div class="back-name">Vastrelby<br>Fieldseal</div>
    <p class="back-web">www.vastrelbyfieldseal.com.au</p>
  </section>

  <section class="card card--front" aria-label="Business card front">
    <div class="brand">
      <span class="brand-mark"></span>
      <span class="brand-name">Vastrelby<br>Fieldseal</span>
    </div>

    <div class="divider"></div>

    <div class="details">
      <h1 class="person-name">Daniel Hartley</h1>
      <p class="person-role">Manager</p>
      <address class="address">52 Harwell Road,<br>Ashvale, WA 6170</address>
      <ul class="contacts">
        <li>
          <svg viewBox="0 0 24 24" aria-hidden="true"><path fill="#2bb24c" d="M6.6 10.8a15 15 0 0 0 6.6 6.6l2.2-2.2c.3-.3.7-.4 1-.2 1.1.4 2.3.6 3.6.6.6 0 1 .4 1 1V20c0 .6-.4 1-1 1C10.6 21 3 13.4 3 4c0-.6.4-1 1-1h3.5c.6 0 1 .4 1 1 0 1.3.2 2.5.6 3.6.1.3 0 .7-.2 1z"/></svg>
          1300 482 619
        </li>
        <li>
          <svg viewBox="0 0 24 24" aria-hidden="true"><rect x="3" y="5" width="18" height="14" rx="1.5" fill="none" stroke="#2bb24c" stroke-width="2"/><path d="M3.5 6l8.5 7 8.5-7" fill="none" stroke="#2bb24c" stroke-width="2"/></svg>
          daniel@vastrelbyfieldseal.com.au
        </li>
        <li>
          <svg viewBox="0 0 24 24" aria-hidden="true"><g fill="none" stroke="#2bb24c" stroke-width="1.8"><circle cx="12" cy="12" r="9"/><ellipse cx="12" cy="12" rx="4" ry="9"/><path d="M3 12h18M5 7h14M5 17h14"/></g></svg>
          www.vastrelbyfieldseal.com.au
        </li>
      </ul>
    </div>
  </section>

</body>
</html>
```